Redesign of Plastic Surgeon Website to fully responsive / modern feel

Hi

Our current website is out of date www.harbourlinecosmetic.org

We want a fresh / modern looking design
Needs to be fully responsive design that works extremely well on ipad and mobile device

Would like design for both full screen website and mobile

Have listed a few websites of other plastic surgeons we like
http://www.reformclinicdaily.com/
http://www.peterholtbymd.com/
http://www.corvanbeauty.com/
http://www.tidewellcontouring.com/

Menu needs to include
1. About Us
2. Procedures (see current website for example)
3. News
4. Patient Resources
5. Contact Us

We are flexible with colours / images / layout

I have uploaded a document that has some content - the face pages content is completed only

some of the procedures can have content upwards of 4000 words - total website can be large with over 40,000 words
Updates

Target Market(s)

Mainly women 20-60 85% of practice
Some men 15%

Industry/Entity Type

Plastic Surgery

Number of Pages Required

5+ page

Requirements
Must have
• We need designs for
• Homepage
• Internal pages
• 1. Landing pages for breast / body / face / non surgical main pages
• 2. Procedure pages for individual pages under each section - eg breast augmentation
• 3. About us pages - like meet the doctor, our staff, clinics
• 4. Contact page
• 5. Blog / News page
Nice to have
• See our list of websites for examples of designs we like
• Like full screen design with nice hero image
• Needs to have good to call to action messages on home page like
• Specials, procedure of the month, etc

```html
<!DOCTYPE html>
<html lang="en">
<head>
<meta charset="utf-8">
<title>Harbourline Institute of Cosmetic Surgery</title>
<link href="https://fonts.googleapis.com/css2?family=Cinzel:wght@400&family=Roboto:wght@400;500;700&family=Open+Sans:wght@400&family=Raleway:wght@400&display=swap" rel="stylesheet">
<style>
:root{
  --ink:#111111;
  --hero-bg:#242424;
  --nav-bg:#1c1c1c;
  --accent:#8e5068;
  --accent-text:#7a3d57;
  --line:#cfcfcf;
  --nav-line:#5a5a5a;
  --body-text:#333333;
  --white:#ffffff;
  --muted:#d6d6d6;
  --footer:#0b0b0b;
  --btn-blue:#2f6fb6;
}
*{box-sizing:border-box;margin:0;padding:0}
html,body{width:1200px;height:2278px;overflow:hidden;background:var(--white)}
body{position:relative;font-family:"Roboto",Arial,sans-serif;color:var(--body-text)}
.abs{position:absolute}

/* hero */
.hero{left:0;top:0;width:1200px;height:747px;background:var(--hero-bg);overflow:hidden}
.hero-photo{left:330px;top:0;width:870px;height:747px;
  background:radial-gradient(ellipse 360px 420px at 260px 340px,#6a5a55 0%,#453a37 45%,#262222 80%,#222 100%)}
.hero-side{left:0;top:0;width:340px;height:747px;background:linear-gradient(90deg,var(--nav-bg) 70%,rgba(28,28,28,0))}
.brand{left:44px;top:40px;width:280px;text-align:center;font-family:"Roboto",Arial,sans-serif;font-weight:400;
  color:var(--white);font-size:17px;line-height:30px;letter-spacing:2px;text-transform:uppercase}
.nav{left:44px;top:202px;width:280px;list-style:none}
.nav li{height:76px;border-bottom:1px solid var(--nav-line);display:flex;align-items:center;padding-left:41px;
  font-size:15px;color:var(--white);text-transform:uppercase;letter-spacing:.2px}
.nav li.active{height:68px;background:var(--accent);border-bottom:none}
.nav li:nth-child(2){height:79px;padding-top:8px}
.contact-bar{left:928px;top:22px;display:flex;align-items:center;gap:10px;color:var(--white);font-size:13px}
.social{display:flex;align-items:center;justify-content:center}
.social-top{top:23px;width:24px;height:24px}
.social-top.filled{left:1089px;background:var(--accent)}
.social-top.outline{left:1126px;border:1px solid var(--white)}
.hero-title{left:442px;top:328px;font-family:"Cinzel",Georgia,serif;font-weight:400;font-size:44px;color:var(--white);letter-spacing:1px;white-space:nowrap}
.hero-text{left:443px;top:396px;width:680px;font-family:"Raleway",Arial,sans-serif;font-size:13px;line-height:24px;color:var(--white);white-space:nowrap}
.btn-hero{left:447px;top:468px;width:132px;height:44px;background:var(--white);border:2px solid var(--btn-blue);
  color:var(--accent-text);font-size:11px;display:flex;align-items:center;justify-content:center;text-transform:uppercase}
.dots{left:636px;top:707px;display:flex;gap:8px}
.dot{width:15px;height:15px;border-radius:50%;border:1.5px solid var(--white)}
.dot.on{background:var(--white)}

/* section headings */
.section-head{left:47px;width:1104px;height:40px;display:flex;align-items:center;justify-content:center}
.section-head::before{content:"";position:absolute;left:0;right:0;top:50%;height:1px;background:var(--line)}
.section-head .label{position:relative;background:var(--white);padding:0 14px;display:flex;align-items:center;gap:14px;
  font-size:31px;font-weight:400;color:var(--ink);letter-spacing:.3px}
.flourish{display:inline-block;width:64px;height:14px;border-radius:7px;background:#3a3a3a}

.intro{left:120px;top:893px;width:960px;text-align:center;font-family:"Open Sans",Arial,sans-serif;font-size:12.5px;line-height:28.5px;color:var(--body-text)}
.btn-dark{left:544px;top:1051px;width:112px;height:34px;background:var(--ink);color:var(--white);font-size:10.5px;
  display:flex;align-items:center;justify-content:center;text-transform:uppercase}

/* services */
.tile{overflow:hidden;color:var(--white);display:flex;flex-direction:column;align-items:center;justify-content:center;text-align:center}
.tile-face{left:47px;top:1223px;width:678px;height:509px;background:radial-gradient(ellipse at 40% 45%,#3b3533,#1d1b1b 75%)}
.tile-body{left:729px;top:1223px;width:422px;height:251px;background:linear-gradient(135deg,#b9a292,#8d7564 60%,#7c6b61)}
.tile-breast{left:729px;top:1480px;width:422px;height:252px;background:linear-gradient(160deg,#9c6c59,#7e5446 55%,#8a6a5a)}
.tile-title{font-size:28px;font-weight:700;text-transform:uppercase;letter-spacing:.3px}
.tile-text{font-size:11.5px;line-height:22px;margin-top:18px;white-space:nowrap}
.btn-light{margin-top:14px;width:114px;height:37px;background:var(--muted);color:#333;font-size:11px;display:flex;align-items:center;justify-content:center;text-transform:uppercase}

/* gallery */
.gallery{left:0;top:1770px;width:1200px;height:246px;background:linear-gradient(90deg,#1a1a18,#2a2622 55%,#1b1a18)}
.gallery-title{left:52px;top:1836px;font-size:46px;color:var(--white);font-weight:400}
.gallery-text{left:53px;top:1912px;font-size:15px;line-height:23px;color:var(--white);white-space:nowrap}
.thumb{top:1821px;width:113px;height:94px;border:2px solid var(--white)}
.thumb.t1{left:676px;background:linear-gradient(135deg,#d9c5b4,#8a7a6c)}
.thumb.t2{left:826px;background:linear-gradient(135deg,#f0d8cc,#c07f7a)}
.thumb.t3{left:975px;background:linear-gradient(135deg,#e8cdb2,#b78f72)}
.btn-outline{left:826px;top:1956px;width:123px;height:38px;border:1.5px solid var(--white);color:var(--white);font-size:13px;
  display:flex;align-items:center;justify-content:center;text-transform:uppercase}

/* partners */
.arrow{top:2084px;width:24px;height:28px;background:#ececec;display:flex;align-items:center;justify-content:center}
.partner{top:2066px;width:183px;height:73px;border:1px solid #dcdcdc;display:flex;align-items:center;justify-content:center}
.partner span{width:128px;height:28px;background:#1a1a1a;border-radius:4px}

/* footer */
.footer{left:0;top:2184px;width:1200px;height:94px;background:var(--footer)}
.footer-text{left:0;top:2222px;width:1200px;text-align:center;font-family:"Open Sans",Arial,sans-serif;font-size:11.5px;color:var(--muted)}
.social-foot{top:2215px;width:28px;height:28px;border:1px solid var(--white)}
</style>
</head>
<body>

<header class="abs hero">
  <div class="abs hero-photo" role="img" aria-label="Portrait of a woman with clear skin, hand resting on her cheek"></div>
  <div class="abs hero-side"></div>

  <div class="abs brand">Harbourline<br>Institute of<br>Cosmetic<br>Surgery</div>

  <ul class="abs nav">
    <li class="active">Home</li>
    <li>About</li>
    <li>Procedures</li>
    <li>News</li>
    <li>Patient Resources</li>
    <li>Contact</li>
  </ul>

  <div class="abs contact-bar">
    <svg width="28" height="28" viewBox="0 0 28 28" aria-hidden="true">
      <circle cx="14" cy="14" r="12.5" fill="none" stroke="#fff" stroke-width="1.5"/>
      <path d="M10 8.5c.8-.6 1.6-.4 2 .3l1 1.8c.3.6.1 1.2-.4 1.5l-.8.5c.6 1.5 1.8 2.8 3.3 3.5l.5-.8c.3-.5 1-.7 1.5-.4l1.8 1c.7.4.9 1.3.3 2-1.2 1.4-3 1.5-5 .3-2.5-1.5-4.3-3.8-5-6.1-.4-1.5 0-2.7.8-3.6z" fill="#fff"/>
    </svg>
    <span>555-014-2260</span>
  </div>
  <div class="abs social social-top filled" aria-label="Share">
    <svg width="14" height="14" viewBox="0 0 14 14" aria-hidden="true">
      <circle cx="3" cy="7" r="2" fill="#fff"/><circle cx="11" cy="3" r="2" fill="#fff"/><circle cx="11" cy="11" r="2" fill="#fff"/>
      <path d="M3 7L11 3M3 7l8 4" stroke="#fff" stroke-width="1.2"/>
    </svg>
  </div>
  <div class="abs social social-top outline" aria-label="Link">
    <svg width="14" height="14" viewBox="0 0 14 14" aria-hidden="true">
      <path d="M6 8l2-2M5 6L3.5 7.5a2 2 0 0 0 3 3L8 9M9 8l1.5-1.5a2 2 0 0 0-3-3L6 5" fill="none" stroke="#fff" stroke-width="1.3" stroke-linecap="round"/>
    </svg>
  </div>

  <h1 class="abs hero-title">Consectetur Adipiscing</h1>
  <p class="abs hero-text">Lorem ipsum dolor sit amet, consectetur adipiscing elit, sed do eiusmod tempor incididunt ut labore et do-<br>loreLorem ipsum dolor sit amet, consectetur adipiscing elit, sed do eiusmod</p>
  <div class="abs btn-hero">Read More</div>

  <div class="abs dots">
    <span class="dot"></span><span class="dot on"></span><span class="dot"></span><span class="dot"></span><span class="dot"></span>
  </div>
</header>

<section>
  <div class="abs section-head" style="top:832px">
    <div class="label"><span class="flourish" role="img" aria-label="Ornamental flourish"></span>HARBOURLINECOSMETIC<span class="flourish" role="img" aria-label="Ornamental flourish"></span></div>
  </div>
  <p class="abs intro">You can expect beautiful results at the Harbourline Institute of Cosmetic Surgery. With expertise in facelifts, breast augmentation or breast reduction and liposuc-<br>tion body contouring, we offer total care at every step of your transformative journey.<br>Dr Whitcombe is one of Australia’s most eminent specialists in plastic surgery, reconstructive and aesthetic surgery, and is supported by our highly qualified,<br>professional team. As the premier plastic surgery clinic in Sydney, we use only the most revolutionary techniques to minimise scarring, we help you look<br>better, feel better and enjoy a beautiful new you.</p>
  <div class="abs btn-dark">Read More</div>
</section>

<section>
  <div class="abs section-head" style="top:1150px">
    <div class="label"><span class="flourish" role="img" aria-label="Ornamental flourish"></span>OUR SERVICE<span class="flourish" role="img" aria-label="Ornamental flourish"></span></div>
  </div>

  <div class="abs tile tile-face" role="img" aria-label="Close-up of a woman's face with surgical markings">
    <div class="tile-title">Face</div>
    <p class="tile-text">Lorem ipsum dolor sit amet, consectetur adipiscing elit, sed do eiusmod tempor incididunt<br>ut labore et dolore magna aliqua.</p>
    <div class="btn-light">Read More</div>
  </div>
  <div class="abs tile tile-body" role="img" aria-label="Abdomen with dotted surgical markings">
    <div class="tile-title">Body</div>
  </div>
  <div class="abs tile tile-breast" role="img" aria-label="Woman in a bra">
    <div class="tile-title">Breast</div>
  </div>
</section>

<section>
  <div class="abs gallery" role="img" aria-label="Dim background of a surgeon at work"></div>
  <h2 class="abs gallery-title">Photo Gallery</h2>
  <p class="abs gallery-text">Lorem ipsum dolor sit amet, consectetur adipiscing elit, sed do eiusmod<br>tempor incididunt ut labore et dolore magna aliqua.</p>
  <div class="abs thumb t1" role="img" aria-label="Cosmetic injection treatment"></div>
  <div class="abs thumb t2" role="img" aria-label="Lip enhancement close-up"></div>
  <div class="abs thumb t3" role="img" aria-label="Abdomen with surgical markings"></div>
  <div class="abs btn-outline">View All</div>
</section>

<section>
  <div class="abs arrow" style="left:50px">
    <svg width="10" height="14" viewBox="0 0 10 14" aria-hidden="true"><path d="M7 2L2 7l5 5" fill="none" stroke="#999" stroke-width="1.5"/></svg>
  </div>
  <div class="abs partner" style="left:106px"><span></span></div>
  <div class="abs partner" style="left:307px"><span></span></div>
  <div class="abs partner" style="left:507px"><span></span></div>
  <div class="abs partner" style="left:711px"><span></span></div>
  <div class="abs partner" style="left:911px"><span></span></div>
  <div class="abs arrow" style="left:1127px">
    <svg width="10" height="14" viewBox="0 0 10 14" aria-hidden="true"><path d="M3 2l5 5-5 5" fill="none" stroke="#999" stroke-width="1.5"/></svg>
  </div>
</section>

<footer>
  <div class="abs footer"></div>
  <p class="abs footer-text">All Right Reserved. Copyright ©2015 Harbourline</p>
  <div class="abs social social-foot" style="left:987px" aria-label="Share">
    <svg width="14" height="14" viewBox="0 0 14 14" aria-hidden="true">
      <circle cx="3" cy="7" r="2" fill="#fff"/><circle cx="11" cy="3" r="2" fill="#fff"/><circle cx="11" cy="11" r="2" fill="#fff"/>
      <path d="M3 7L11 3M3 7l8 4" stroke="#fff" stroke-width="1.2"/>
    </svg>
  </div>
  <div class="abs social social-foot" style="left:1028px" aria-label="Email">
    <svg width="14" height="14" viewBox="0 0 14 14" aria-hidden="true">
      <rect x="1.5" y="3" width="11" height="8" fill="none" stroke="#fff" stroke-width="1.2"/>
      <path d="M1.5 3.5L7 8l5.5-4.5" fill="none" stroke="#fff" stroke-width="1.2"/>
    </svg>
  </div>
  <div class="abs social social-foot" style="left:1071px" aria-label="Link">
    <svg width="14" height="14" viewBox="0 0 14 14" aria-hidden="true">
      <path d="M6 8l2-2M5 6L3.5 7.5a2 2 0 0 0 3 3L8 9M9 8l1.5-1.5a2 2 0 0 0-3-3L6 5" fill="none" stroke="#fff" stroke-width="1.3" stroke-linecap="round"/>
    </svg>
  </div>
</footer>

</body>
</html>
```